依頼詳細
会社の封筒デザインを依頼します。封筒は「シンプル」だけど「先進的」なデザインを希望します。封筒は淡い水色です。発注先の印刷会社さんはグラデーションがあるとコスト高になりますので、グラデーションは入れないでください。また、黒1色で考えておりますので宜しくお願いします。
長3の封筒は横むきでお願いします。
記載項目
表面:会社名/〒住所/電話/Fax/URL
サイズ
希望イメージ
• +5 0 +5
• シンプル
複雑
• 単色
カラフル
• 暗い
明るい
• 日常
高級
• 遊び心
厳粛
• 未来的
伝統的
• 女性的
男性的
納品ファイル
• 高解像度JPG (.jpg)
• イラストレーター形式 (.ai)
補足説明
住所や氏名を記載する場合の下線を薄めか、点線で入れ、端に御中の文字を入れて下さい。
依頼公開後の追記内容
ロゴデータ追加致しました
ファイルの追加が出来ていませんでしたので、再度投稿しました。
【イメージの追記】
イメージですが、透き通ったような?スタイリッシュな?都会的な?繊細な?
簡単にいうと、かっこいい?ようなイメージでお願いできたらと思います。
言葉で伝えるって難しいですね。
表現力が無くてすみません。

申し訳ございませんが、締切日を延期させていただきました。
これまでご提案下さいました方には、ご了承の程宜しくお願い致します。
■ 選んだ理由

シンプルで、弊社のイメージしていたものを表現してくれたようなデザインでした。

■ 提案者全員のお礼・コメント

どれもこれも素敵なデザインばかりで選ぶのが大変でした。
皆様のデザインに感謝いたします。ありがとうございました。
今後も、機会がございましたら、宜しくお願い致します。

```html
<!DOCTYPE html>
<html lang="ja">
<head>
<meta charset="utf-8">
<title>封筒デザイン</title>
<link href="https://fonts.googleapis.com/css2?family=Noto+Sans+JP:wght@400;700;900&display=swap" rel="stylesheet">
<style>
  :root {
    --paper: #d3e8f7;
    --paper-fold: #c6dff1;
    --ink: #1a1a1a;
    --rule: #9fb6c7;
    --page: #ffffff;
  }
  html, body {
    margin: 0;
    padding: 0;
    width: 804px;
    height: 1200px;
    overflow: hidden;
    background: var(--page);
    font-family: "Noto Sans JP", sans-serif;
    color: var(--ink);
  }
  .envelope {
    position: relative;
    width: 804px;
    height: 1200px;
  }
  .envelope-shape {
    position: absolute;
    inset: 0;
  }
  .address-lines {
    position: absolute;
    left: 113px;
    top: 0;
    width: 557px;
  }
  .address-line {
    position: absolute;
    left: 0;
    width: 557px;
    border-top: 2px dashed var(--rule);
  }
  .address-line.first { top: 538px; }
  .address-line.second { top: 626px; }
  .address-line.third { top: 714px; }
  .honorific {
    position: absolute;
    right: 134px;
    top: 656px;
    font-size: 34px;
    font-weight: 400;
    letter-spacing: 2px;
  }
  .sender {
    position: absolute;
    left: 140px;
    top: 932px;
    width: 560px;
  }
  .company {
    display: flex;
    align-items: center;
    gap: 16px;
    height: 66px;
  }
  .company-dot {
    width: 50px;
    height: 50px;
    border-radius: 50%;
    background: var(--ink);
    flex: none;
  }
  .company-name {
    font-size: 50px;
    font-weight: 900;
    letter-spacing: 1px;
    line-height: 1;
    white-space: nowrap;
  }
  .contact {
    display: grid;
    grid-template-columns: 118px auto;
    margin-top: 24px;
    font-size: 22px;
    line-height: 27px;
  }
  .contact .postal {
    font-size: 17px;
    padding-top: 3px;
  }
  .contact .details > span {
    display: block;
    white-space: nowrap;
  }
  .contact .fax { margin-left: 20px; }
</style>
</head>
<body>
  <main class="envelope">
    <svg class="envelope-shape" width="804" height="1200" viewBox="0 0 804 1200" aria-hidden="true">
      <rect x="0" y="100" width="804" height="1100" fill="var(--paper)"/>
      <polygon points="0,100 22,0 782,0 804,100" fill="var(--paper-fold)"/>
      <line x1="0" y1="100" x2="804" y2="100" stroke="#b9d3e6" stroke-width="1.5"/>
    </svg>

    <div class="address-lines">
      <div class="address-line first"></div>
      <div class="address-line second"></div>
      <div class="address-line third"></div>
    </div>
    <div class="honorific">御中</div>

    <section class="sender">
      <div class="company">
        <span class="company-dot"></span>
        <span class="company-name">○○○○株式会社</span>
      </div>
      <div class="contact">
        <span class="postal">〒150-0042</span>
        <div class="details">
          <span>東京都渋谷区青葉台南町5-8-214</span>
          <span>Tel.03-2217-4806<span class="fax">Fax.03-2217-4807</span></span>
          <span>URL.http://www.sorairo-ex.jp</span>
        </div>
      </div>
    </section>
  </main>
</body>
</html>
```